New Design for Brightcove Heating [Plimsy]

Hello, This is my 2nd project here. I need a new web design for www.brightcoveheating.com.au which is one of my clients, and an extremely outdated website. It only has a few links and is fairly straight forward, looking for a more professional, up-to-date looking website. Please note: The website will be made under a plimsy white-label platform, so the design MUST be consistent with this type of platform. Many more projects will be up and coming so the best designers will definitely be selected for future projects.
Thankyou

Industry/Entity Type

It Professional

Requirements
Must have
• Please refer to www.brightcoveheating.com.au to find all the content.

```html
<!DOCTYPE html>
<html lang="en">
<head>
<meta charset="utf-8">
<title>Emberfield Heating Pty Ltd</title>
<link href="https://fonts.googleapis.com/css2?family=PT+Sans:wght@400;700&family=Tinos&family=Arimo:wght@400;700&display=swap" rel="stylesheet">
<style>
:root{
  --page-bg:#1f1f1f;
  --white:#ffffff;
  --panel:#f2f2f2;
  --footer:#d9d9d9;
  --text:#2b2b2b;
  --heading:#1a1a1a;
  --orange-dark:#d97c00;
  --brand-blue:#1656d6;
  --bullet:#2f8fd8;
  --frame:#e4e4e4;
  --muted-grey:#6d6d6d;
}
*{margin:0;padding:0;box-sizing:border-box}
html,body{width:1015px;height:1200px;overflow:hidden}
body{position:relative;background:var(--page-bg) radial-gradient(circle at 50% 30%,#2a2a2a,#181818);font-family:"PT Sans",sans-serif;color:var(--text)}
.abs{position:absolute}
.company-name{left:75px;top:14px;color:var(--white);font-size:18px;white-space:nowrap}
.brand-square{left:116px;top:48px;width:75px;height:75px;background:var(--brand-blue);border:3px solid var(--white)}
.search{left:751px;top:18px;width:191px;height:30px;background:var(--white);border:1px solid #ccc}
.search span{position:absolute;left:11px;top:7px;font-size:11px;font-style:italic;color:#666}
.search svg{position:absolute;right:8px;top:4px}
.nav a{position:absolute;top:88px;color:var(--white);font-size:17px;text-decoration:none}
.nav .home{left:386px;top:84px;width:94px;height:34px;line-height:32px;text-align:center;border-radius:8px;background:linear-gradient(#fbb23a,var(--orange-dark));box-shadow:0 2px 4px rgba(0,0,0,.6)}
.banner{left:75px;top:145px;width:867px;height:268px;background:var(--frame);padding:6px;box-shadow:0 22px 22px -10px rgba(0,0,0,.7)}
.banner div{width:100%;height:100%;background:linear-gradient(180deg,#e9eef4 0%,#b9c0c8 40%,#8aa0b8 65%,#c4b8a2 100%)}
.panel{left:74px;top:473px;width:868px;height:554px;background:var(--panel);border-radius:10px 10px 0 0}
.footer{left:74px;top:1027px;width:868px;height:128px;background:var(--footer);border-radius:0 0 10px 10px}
.serif{font-family:"Tinos",serif;color:var(--heading);font-weight:400;white-space:nowrap}
.welcome{left:94px;top:488px;font-size:26px}
.intro{left:94px;top:534px;width:535px;font-size:11.5px;line-height:17px}
.products-title{left:94px;top:627px;font-size:18px}
.product-list{left:97px;top:662px;list-style:none;font-size:11.5px;white-space:nowrap}
.product-list li{height:27.7px;display:flex;align-items:center}
.product-list li::before{content:"";width:13px;height:12px;margin-right:16px;border-radius:2px;background:linear-gradient(#6cc3f5,var(--bullet));border:1px solid #1a6fb0}
.tile{left:431px;width:173px;height:106px;border-radius:9px;border:2px solid #333;overflow:hidden;background:#3a3a3a}
.tile .img{position:absolute;inset:0}
.tile span{position:absolute;left:0;right:0;bottom:0;height:22px;line-height:22px;text-align:right;padding-right:6px;color:var(--white);font-size:10.5px;font-weight:700;background:rgba(0,0,0,.6);white-space:nowrap}
.specialists-title{left:655px;top:495px;font-size:18px}
.spec-list{left:657px;top:528px;list-style:none;font-size:11.5px;white-space:nowrap}
.spec-list li{height:27.7px;display:flex;align-items:center}
.spec-list svg{margin-right:16px}
.brand-square-small{left:107px;top:1058px;width:69px;height:69px;background:var(--muted-grey)}
.foot{font-family:"Arimo",sans-serif;font-size:12px;line-height:15px;color:#111;white-space:nowrap}
.address{left:183px;top:1064px;font-weight:700;font-style:normal}
.contact{left:421px;top:1064px}
.contact b{display:inline-block;width:48px}
.contact u{color:#555;font-weight:700}
.copyright{left:686px;top:1057px;width:240px;font-size:11px;line-height:26px;text-align:center;font-family:"PT Sans",sans-serif;white-space:nowrap}
</style>
</head>
<body>
<div class="abs company-name">Emberfield Heating Pty Ltd</div>
<div class="abs brand-square"></div>

<div class="abs search"><span>search..</span>
<svg width="24" height="22" viewBox="0 0 24 22"><circle cx="9" cy="8" r="6" fill="none" stroke="#222" stroke-width="3"/><line x1="13" y1="12" x2="20" y2="19" stroke="#222" stroke-width="4" stroke-linecap="round"/></svg>
</div>

<nav class="nav">
<a class="home" href="#">Home</a>
<a href="#" style="left:512px">Products</a>
<a href="#" style="left:634px">Services</a>
<a href="#" style="left:751px">Blog</a>
<a href="#" style="left:841px">Contact us</a>
</nav>

<div class="abs banner"><div role="img" aria-label="Photo of a bright fabrication workshop floor with machines"></div></div>

<main class="abs panel"></main>
<h1 class="abs serif welcome">Welcome to Emberfield Heating</h1>
<p class="abs intro">Emberfield Heating are one of Australia's leading suppliers and manufacturers of thermal fabrics and fabrications. The experience, knowledge and facility to design and fabricate gives you the quality Australian made products you demand.</p>
<h2 class="abs serif products-title">Thermal Product available at Emberfield Heating</h2>
<ul class="abs product-list">
<li>Ceramic Fibre Tapes, Ropes, Braids, Boards &amp; Insulation.</li>
<li>Glass Fibre Tapes, Ropes, Braids, Boards &amp; Insulation.</li>
<li>Furnace / Oven Tadpole Tape Seals.</li>
<li>Boiler Tapes, Seals &amp; Gaskets.</li>
<li>Boiler Close Up Kits.</li>
<li>Welding Blankets, Curtains &amp; Screens</li>
<li>Exhaust Thermal / Acoustic Covers.</li>
<li>Thermal Hoods / Covers.</li>
<li>Machine Thermal Covers.</li>
<li>Thermal Fabrics.</li>
<li>Thermal Fabrications - To your Specification</li>
<li>Fabric / Metallic Expansion Joints &amp; Associated Metal Work</li>
</ul>

<div class="abs tile" style="top:671px"><div class="img" role="img" aria-label="Photo of a boiler close up kit with tub and rope" style="background:linear-gradient(135deg,#5a4a3e,#d8d4cc 50%,#6a5a4c)"></div><span>Boiler Close Up Kits</span></div>
<div class="abs tile" style="top:783px"><div class="img" role="img" aria-label="Photo of a fabric expansion joint type CR1" style="background:linear-gradient(180deg,#8a8a8a,#d6d6d6 45%,#6e6e6e)"></div><span>Fabric Expansion Joint - Type CR1</span></div>
<div class="abs tile" style="top:895px"><div class="img" role="img" aria-label="Photo of a fabric expansion joint type B1" style="background:linear-gradient(160deg,#3a3a3a,#c8c8d0 50%,#7a7a82)"></div><span>Fabric Expansion Joint - Type B1</span></div>

<h2 class="abs serif specialists-title">Thermal and Sealing Specialists</h2>
<ul class="abs spec-list">
<li><svg width="12" height="12"><rect x=".5" y=".5" width="11" height="11" fill="#fff" stroke="#8898b8"/><path d="M3 6l2 2 4-5" fill="none" stroke="#2a4aa8" stroke-width="1.5"/></svg>Thermal Fabrics and Fabrications</li>
<li><svg width="12" height="12"><rect x=".5" y=".5" width="11" height="11" fill="#fff" stroke="#8898b8"/><path d="M3 6l2 2 4-5" fill="none" stroke="#2a4aa8" stroke-width="1.5"/></svg>High and Low Temperature Insulation</li>
<li><svg width="12" height="12"><rect x=".5" y=".5" width="11" height="11" fill="#fff" stroke="#8898b8"/><path d="M3 6l2 2 4-5" fill="none" stroke="#2a4aa8" stroke-width="1.5"/></svg>Furnace / Oven Door Seals</li>
<li><svg width="12" height="12"><rect x=".5" y=".5" width="11" height="11" fill="#fff" stroke="#8898b8"/><path d="M3 6l2 2 4-5" fill="none" stroke="#2a4aa8" stroke-width="1.5"/></svg>Welding Blankets and Curtains</li>
<li><svg width="12" height="12"><rect x=".5" y=".5" width="11" height="11" fill="#fff" stroke="#8898b8"/><path d="M3 6l2 2 4-5" fill="none" stroke="#2a4aa8" stroke-width="1.5"/></svg>Fabric Expansion Joints</li>
<li><svg width="12" height="12"><rect x=".5" y=".5" width="11" height="11" fill="#fff" stroke="#8898b8"/><path d="M3 6l2 2 4-5" fill="none" stroke="#2a4aa8" stroke-width="1.5"/></svg>Boat Exhaust Covers</li>
<li><svg width="12" height="12"><rect x=".5" y=".5" width="11" height="11" fill="#fff" stroke="#8898b8"/><path d="M3 6l2 2 4-5" fill="none" stroke="#2a4aa8" stroke-width="1.5"/></svg>Thermal Hoods / Covers</li>
<li><svg width="12" height="12"><rect x=".5" y=".5" width="11" height="11" fill="#fff" stroke="#8898b8"/><path d="M3 6l2 2 4-5" fill="none" stroke="#2a4aa8" stroke-width="1.5"/></svg>Acoustic Materials</li>
<li><svg width="12" height="12"><rect x=".5" y=".5" width="11" height="11" fill="#fff" stroke="#8898b8"/><path d="M3 6l2 2 4-5" fill="none" stroke="#2a4aa8" stroke-width="1.5"/></svg>Pump and Valve Packings</li>
<li><svg width="12" height="12"><rect x=".5" y=".5" width="11" height="11" fill="#fff" stroke="#8898b8"/><path d="M3 6l2 2 4-5" fill="none" stroke="#2a4aa8" stroke-width="1.5"/></svg>Gasket Materials</li>
<li><svg width="12" height="12"><rect x=".5" y=".5" width="11" height="11" fill="#fff" stroke="#8898b8"/><path d="M3 6l2 2 4-5" fill="none" stroke="#2a4aa8" stroke-width="1.5"/></svg>Standard and Non-Standard Gaskets</li>
<li><svg width="12" height="12"><rect x=".5" y=".5" width="11" height="11" fill="#fff" stroke="#8898b8"/><path d="M3 6l2 2 4-5" fill="none" stroke="#2a4aa8" stroke-width="1.5"/></svg>Boilers Gaskets and Seals</li>
<li><svg width="12" height="12"><rect x=".5" y=".5" width="11" height="11" fill="#fff" stroke="#8898b8"/><path d="M3 6l2 2 4-5" fill="none" stroke="#2a4aa8" stroke-width="1.5"/></svg>Spiral Wounds</li>
<li><svg width="12" height="12"><rect x=".5" y=".5" width="11" height="11" fill="#fff" stroke="#8898b8"/><path d="M3 6l2 2 4-5" fill="none" stroke="#2a4aa8" stroke-width="1.5"/></svg>Ember Seal</li>
<li><svg width="12" height="12"><rect x=".5" y=".5" width="11" height="11" fill="#fff" stroke="#8898b8"/><path d="M3 6l2 2 4-5" fill="none" stroke="#2a4aa8" stroke-width="1.5"/></svg>and Lots more</li>
</ul>

<footer class="abs footer"></footer>
<div class="abs brand-square-small"></div>
<address class="abs foot address">Emberfield Heating Pty Ltd<br>18 Harlow Court<br>Keysborough &nbsp;&nbsp;&nbsp;&nbsp;3173<br>Victoria &nbsp;&nbsp;&nbsp;&nbsp;Australia</address>
<div class="abs foot contact"><b>Phone:</b>+61 3 9000 4127<br><b>Fax:</b>+61 3 9000 4128<br><b>Email:</b> <u>sales@emberfieldheating.com.au</u><br><b style="width:auto">Contact:</b> Alan Pryce - Dana Pryce</div>
<div class="abs copyright">Copyright © 2011 www.emberfieldheating.com<br>All rights reserved</div>
</body>
</html>
```